Boutique Recruiting Firm Needs Eye-Catching Business Cards (and potentially new logo)!

I run a recruiting company in Charleston, South Carolina. I have a ton of networking events coming up and need business cards to grab potential clients attention.

I currently have a logo but if you want to try and recreate the logo to something more modern I am open to that. If you do decide to create a new logo please submit the business card with the old logo and the new one.

Staffing Beyond the Lantern, LLC is the name of my company. I create videos to my clients and candidates which allows me to standout from my competition so I would like a business card (and possibly new logo) to do the same.

I do not specialize in any one industry of recruiting.

Industry/Entity Type

Business

```html
<!DOCTYPE html>
<html lang="en">
<head>
<meta charset="utf-8">
<title>Staffing Beyond the Lantern, LLC — Business Card</title>
<link href="https://fonts.googleapis.com/css2?family=Open+Sans:wght@400;600&display=swap" rel="stylesheet">
<style>
  :root {
    --backdrop: #4a403b;
    --card: #0d0d0d;
    --card-edge: #1a1a1a;
    --ink: #f2f2f2;
    --ink-soft: #cfcfcf;
    --rule: #6a6a6a;
  }
  * { box-sizing: border-box; margin: 0; padding: 0; }
  html, body {
    width: 1200px; height: 814px; overflow: hidden;
    background: var(--backdrop);
    font-family: "Open Sans", Arial, sans-serif;
  }
  .canvas {
    position: relative; width: 1200px; height: 814px;
    display: flex; align-items: center; justify-content: center; gap: 60px;
  }
  .card {
    position: relative;
    width: 520px; height: 298px;
    background: var(--card);
    border: 1px solid var(--card-edge);
    box-shadow: 0 10px 30px rgba(0,0,0,.45);
    color: var(--ink);
  }
  .wordmark {
    display: flex; align-items: center; gap: 10px;
    color: var(--ink); font-weight: 600; line-height: 1.15;
  }
  .wordmark__square {
    width: 16px; height: 16px; background: var(--ink); flex: none;
  }
  /* front */
  .card--front .wordmark {
    position: absolute; left: 40px; top: 180px; font-size: 17px; width: 200px;
  }
  .card--front .divider {
    position: absolute; left: 255px; top: 34px; width: 1px; height: 220px;
    background: linear-gradient(var(--rule), rgba(106,106,106,.3));
  }
  .contact {
    position: absolute; left: 275px; top: 34px; font-size: 13px; color: var(--ink-soft);
  }
  .contact__name { font-size: 17px; font-weight: 600; color: var(--ink); }
  .contact__role { margin-bottom: 10px; }
  .contact__address { line-height: 1.45; margin-bottom: 8px; }
  .contact__list { list-style: none; }
  .contact__list li { display: flex; align-items: center; gap: 8px; line-height: 1.55; }
  .contact__list svg { width: 12px; height: 12px; fill: var(--ink); flex: none; }
  /* back */
  .card--back { display: flex; flex-direction: column; align-items: center; justify-content: center; }
  .card--back .wordmark { font-size: 24px; margin-top: -10px; }
  .card--back .web {
    margin-top: 38px; font-size: 11px; letter-spacing: 3px; color: var(--ink-soft);
  }
</style>
</head>
<body>
<main class="canvas">
  <section class="card card--front" aria-label="Card front">
    <div class="wordmark"><span class="wordmark__square"></span><span>Staffing Beyond the Lantern, LLC</span></div>
    <div class="divider"></div>
    <div class="contact">
      <p class="contact__name">Daniel Reyes</p>
      <p class="contact__role">CEO/Founder</p>
      <p class="contact__address">214 Harbor View Road<br>Charleston, SC 29401</p>
      <ul class="contact__list">
        <li><svg viewBox="0 0 12 12"><path d="M2.5 1 4.5 3 3.6 4.4c.8 1.6 2.2 3 3.9 3.9L8.9 7.5l2 2-1.4 1.5C5 10.8 1.2 7 1 2.4z"/></svg>843 555 0172</li>
        <li><svg viewBox="0 0 12 12"><path d="M3.5 0h5a1 1 0 0 1 1 1v10a1 1 0 0 1-1 1h-5a1 1 0 0 1-1-1V1a1 1 0 0 1 1-1zm.5 1.5v8h4v-8zM6 10.2a.6.6 0 1 0 0 1.2.6.6 0 0 0 0-1.2z"/></svg>843 555 0198</li>
        <li><svg viewBox="0 0 12 12"><path d="M3 0h5v3H3zM1 4h10v6H1zm2 1.5v1h2v-1zM3 11h6v1H3z"/></svg>843 555 0133</li>
        <li><svg viewBox="0 0 12 12"><path d="M0 2h12v8H0zm1.2 1 4.8 3.6L10.8 3z"/></svg>hello@beyondlantern.com</li>
        <li><svg viewBox="0 0 12 12"><path d="M6 0a6 6 0 1 0 0 12A6 6 0 0 0 6 0zm0 1.2c.7 0 1.5 1.4 1.7 3.3H4.3C4.5 2.6 5.3 1.2 6 1.2zM4.3 5.7h3.4C7.5 7.6 6.7 10.8 6 10.8S4.5 7.6 4.3 5.7zM1.3 5.7h1.8c.1 1.6.5 3 1 4A4.8 4.8 0 0 1 1.3 5.7zm7.6 0h1.8a4.8 4.8 0 0 1-2.8 4c.5-1 .9-2.4 1-4zM1.3 4.5A4.8 4.8 0 0 1 4.1 2.3c-.5 1-.9 2.3-1 2.2zm7.6 0c-.1-.9-.5-2.2-1-2.2a4.8 4.8 0 0 1 2.8 2.2z"/></svg>www.beyondlantern.com</li>
      </ul>
    </div>
  </section>
  <section class="card card--back" aria-label="Card back">
    <div class="wordmark"><span class="wordmark__square"></span><span>Staffing Beyond the Lantern, LLC</span></div>
    <p class="web">www.beyondlantern.com</p>
  </section>
</main>
</body>
</html>
```